Boutique town planning business needs a Business Card design

We need a business card design for a new company called The Zoning Bridgeway. We provide town planning and urban design services to government, business and community groups. We would like to see the designs use the colours in the logo (blue, deep red, green and amber), plenty of white and including black and grey in the writing. The final design should communicate collaboration, creativity and professionalism and that we are approachable.

Industry/Entity Type

Town

```html
<!DOCTYPE html>
<html lang="en">
<head>
<meta charset="utf-8">
<title>The Zoning Bridgeway – Business Card</title>
<link rel="stylesheet" href="https://fonts.googleapis.com/css2?family=Exo+2:wght@400;500;600&display=swap">
<style>
  :root {
    --page-bg: #e4e6e9;
    --card-white: #ffffff;
    --card-black: #0c0c0c;
    --accent-red: #8e4a44;
    --text-grey: #3a3a3a;
    --text-dark: #222222;
    --brand-blue: #2b8fc4;
    --light-grey: #c9cacc;
  }
  * { margin: 0; padding: 0; box-sizing: border-box; }
  html, body {
    width: 1200px; height: 864px; overflow: hidden;
    background: var(--page-bg);
    font-family: "Exo 2", sans-serif;
  }
  .business-card {
    position: absolute; left: 100px; top: 146px;
    width: 1000px; height: 572px;
    background: var(--card-black);
    box-shadow: 0 18px 40px rgba(0,0,0,0.18);
    overflow: hidden;
  }
  .card-shapes { position: absolute; inset: 0; }
  .brand {
    position: absolute; left: 290px; top: 175px;
    display: flex; align-items: center; gap: 16px;
  }
  .brand-dot {
    width: 62px; height: 62px; border-radius: 50%;
    background: var(--brand-blue);
  }
  .brand-name {
    font-size: 34px; font-weight: 600; color: var(--text-dark);
    line-height: 1.05;
  }
  .contact-list {
    position: absolute; right: 60px; top: 78px;
    list-style: none; text-align: right;
    color: var(--text-grey); font-size: 18px; letter-spacing: 0.5px;
  }
  .contact-list li {
    display: flex; justify-content: flex-end; align-items: center;
    gap: 10px; margin-bottom: 12px;
  }
  .contact-list .address { display: block; font-size: 21px; line-height: 1.3; margin-bottom: 20px; padding-right: 30px; }
  .contact-list svg { width: 18px; height: 18px; fill: var(--accent-red); flex: none; }
  .contact-list .web { padding-right: 28px; font-size: 17px; }
  .holder {
    position: absolute; left: 62px; top: 452px; color: var(--card-white);
  }
  .holder-name { font-size: 30px; font-weight: 500; letter-spacing: 2px; }
  .holder-role { font-size: 20px; letter-spacing: 1px; margin-top: 2px; padding-left: 22px; }
</style>
</head>
<body>
<div class="business-card">
  <svg class="card-shapes" viewBox="0 0 1000 572" width="1000" height="572" aria-hidden="true">
    <defs>
      <linearGradient id="corner-sheen" x1="0" y1="0" x2="1" y2="0">
        <stop offset="0" stop-color="#0c0c0c"/>
        <stop offset="0.45" stop-color="#0c0c0c"/>
        <stop offset="1" stop-color="#d2d3d5"/>
      </linearGradient>
    </defs>
    <rect class="sheen" x="560" y="300" width="440" height="272" fill="url(#corner-sheen)"/>
    <path class="accent-swoosh" fill="var(--accent-red)"
      d="M200,0 C90,150 110,330 300,395 C470,450 760,440 1000,355 L1000,362 C760,460 450,470 285,410 C80,340 70,140 170,0 Z"/>
    <path class="white-field" fill="var(--card-white)"
      d="M215,0 H1000 V340 C770,425 480,432 320,385 C140,330 120,160 215,0 Z"/>
  </svg>

  <div class="brand">
    <span class="brand-dot"></span>
    <span class="brand-name">The Zoning<br>Bridgeway</span>
  </div>

  <ul class="contact-list">
    <li class="address">12 Elm Court<br>Riverside Lane RVS</li>
    <li>012 555 0148
      <svg viewBox="0 0 24 24"><path d="M6.6 10.8a15 15 0 0 0 6.6 6.6l2.2-2.2c.3-.3.7-.4 1-.2 1.1.4 2.3.6 3.6.6.6 0 1 .4 1 1V20c0 .6-.4 1-1 1A17 17 0 0 1 3 4c0-.6.4-1 1-1h3.5c.6 0 1 .4 1 1 0 1.3.2 2.5.6 3.6.1.3 0 .7-.2 1z"/></svg>
    </li>
    <li>012 555 0148
      <svg viewBox="0 0 24 24"><path d="M7 1h10a2 2 0 0 1 2 2v18a2 2 0 0 1-2 2H7a2 2 0 0 1-2-2V3a2 2 0 0 1 2-2zm0 3v14h10V4zm5 15.5a1 1 0 1 0 0 2 1 1 0 0 0 0-2z"/></svg>
    </li>
    <li>012 555 0148
      <svg viewBox="0 0 24 24"><path d="M6 2h9l3 3v5H6zM4 11h16a2 2 0 0 1 2 2v8H2v-8a2 2 0 0 1 2-2zm3 3v2h3v-2zm0 3v2h3v-2zm5-3v2h3v-2z"/></svg>
    </li>
    <li>hello@zoningbridgeway.com
      <svg viewBox="0 0 24 24"><path d="M2 5h20v14H2zm2 2v.5l8 5 8-5V7l-8 5z"/></svg>
    </li>
    <li>www.zoningbridgeway.com
      <svg viewBox="0 0 24 24"><path d="M12 2a10 10 0 1 0 0 20 10 10 0 0 0 0-20zm6.9 9h-3a15 15 0 0 0-1.3-5.8A8 8 0 0 1 18.9 11zM12 4c.9 1.2 1.8 3.6 1.9 7h-3.8c.1-3.4 1-5.8 1.9-7zM9.4 5.2A15 15 0 0 0 8.1 11h-3a8 8 0 0 1 4.3-5.8zM5.1 13h3a15 15 0 0 0 1.3 5.8A8 8 0 0 1 5.1 13zM12 20c-.9-1.2-1.8-3.6-1.9-7h3.8c-.1 3.4-1 5.8-1.9 7zm2.6-1.2a15 15 0 0 0 1.3-5.8h3a8 8 0 0 1-4.3 5.8z"/></svg>
    </li>
  </ul>

  <div class="holder">
    <p class="holder-name">MARTIN KELLER</p>
    <p class="holder-role">Managing Director</p>
  </div>
</div>
</body>
</html>
```